Create Vertical Dog Food Labels (3 inches x 5 inches) for PupKitchen

We need a packing Vertical label (3 inches x 5 inches) design for our line of Dog Food - Pup Kitchen at pupkitchenmeals.com (please review website). This design is for Custom Roll Labels. We have a logo already. Use our logo colors on label. What we need incorporated is a list of our ingredients:

50% Choice Beef
20% Pasture-raised Chicken
15% Brown Rice
15% Fresh Vegetables - Carrots, Kale, Zucchini
Garden Vital Nutrients

We also need these lines at the bottom of the label:

Keeps in fridge for 4 days after thawing
Stores in freezer up to 6 months
Questions? email us at orders@meadowlanepantry.com

We have attached a sample of a competitor. The Kibble Crate.

Target Market(s)

Dog owners

Industry/Entity Type

Dog Food

Font styles to use
Sans Serif

Requirements
Must have
• Read project description above
Nice to have
• Our logo color incorporated
Should not have
• I want it simple.

```html
<!DOCTYPE html>
<html lang="en">
<head>
<meta charset="utf-8">
<title>PupKitchen – Dog Food Label</title>
<link rel="stylesheet" href="https://fonts.googleapis.com/css2?family=Varela+Round&family=Nunito:wght@300&family=Fredoka:wght@600&display=swap">
<style>
  :root {
    --page-bg: #ececec;
    --label-bg: #ffffff;
    --green: #82be41;
    --green-dark: #5c9e3a;
    --brand-green: #0e7a22;
    --beef: #ff5a2c;
    --chicken: #f5c04a;
    --rice: #ffa500;
    --veg: #7dbe3e;
    --ink: #2a2a2a;
    --dog-tone: #f0cf5e;
    --bowl-tone: #e6e6e6;
  }
  * { margin: 0; padding: 0; box-sizing: border-box; }
  html, body { width: 1200px; height: 913px; overflow: hidden; }
  body { background: var(--page-bg); position: relative; font-family: "Varela Round", sans-serif; color: var(--ink); }

  .label {
    position: absolute; left: 342px; top: 26px;
    width: 516px; height: 860px;
    background: var(--label-bg);
    overflow: hidden;
    box-shadow: 0 4px 18px rgba(0,0,0,.12);
  }
  .label-shapes { position: absolute; inset: 0; }

  .brand {
    position: absolute; top: 48px; left: 0; right: 0;
    display: flex; align-items: center; justify-content: center; gap: 12px;
  }
  .brand-dot { width: 44px; height: 44px; border-radius: 50%; background: var(--green); }
  .brand-name { font-family: "Varela Round", sans-serif; font-size: 46px; color: var(--brand-green); letter-spacing: 1px; }

  .title { position: absolute; top: 222px; left: 0; right: 0; text-align: center; color: #fff; }
  .title-main { font-family: "Fredoka", sans-serif; font-weight: 600; font-size: 80px; line-height: 1.05; letter-spacing: 2px; }
  .title-sub { font-family: "Nunito", sans-serif; font-weight: 300; font-size: 38px; line-height: 1; margin-top: 0; }

  .ingredient-chart { position: absolute; left: 49px; top: 400px; width: 174px; height: 174px; }
  .ingredient-chart text { font-family: "Fredoka", sans-serif; font-weight: 600; font-size: 21px; fill: #fff; text-anchor: middle; dominant-baseline: middle; }

  .ingredient-list { position: absolute; left: 234px; top: 420px; list-style: none; font-size: 16px; line-height: 1.2; }
  .ingredient-list li { position: relative; padding-left: 18px; margin-bottom: 12px; }
  .ingredient-list li::before { content: ""; position: absolute; left: 2px; top: 7px; width: 6px; height: 6px; border-radius: 50%; background: var(--dot); }
  .ingredient-list .beef { --dot: var(--beef); }
  .ingredient-list .chicken { --dot: var(--chicken); }
  .ingredient-list .rice { --dot: var(--rice); }
  .ingredient-list .veg { --dot: var(--veg); }

  .storage { position: absolute; left: 50px; top: 622px; list-style: none; font-size: 16px; }
  .storage li { display: flex; align-items: center; gap: 12px; margin-bottom: 16px; }
  .storage-mark { width: 20px; height: 20px; }

  .contact { position: absolute; left: 47px; top: 702px; font-size: 14.5px; }
  .website { position: absolute; left: 50px; top: 740px; display: flex; align-items: center; gap: 12px; font-size: 19px; color: var(--green); }
  .website svg { width: 14px; height: 14px; }

  .bowl-art { position: absolute; left: 243px; top: 818px; width: 72px; height: 28px; border-radius: 50%; background: var(--bowl-tone); }
  .dog-art { position: absolute; left: 354px; top: 735px; width: 122px; height: 115px; border-radius: 40px; background: radial-gradient(circle at 45% 40%, var(--dog-tone), #e3b94a); }
</style>
</head>
<body>
  <main class="label">
    <svg class="label-shapes" viewBox="0 0 516 860" aria-hidden="true">
      <path fill="var(--green)" d="M0 200 C120 172 240 172 320 186 C400 200 460 192 516 180 L516 392 C440 404 380 398 300 382 C200 362 100 370 0 386 Z"/>
      <path fill="var(--green-dark)" d="M300 186 C380 160 460 154 516 168 L516 196 C460 206 390 206 300 186 Z"/>
      <path fill="var(--green)" d="M0 812 C80 798 180 804 260 824 C340 842 430 836 516 818 L516 860 L0 860 Z"/>
      <path fill="var(--green-dark)" d="M140 860 C240 838 380 836 516 842 L516 860 Z"/>
    </svg>

    <header class="brand">
      <span class="brand-dot"></span>
      <span class="brand-name">PupKitchen</span>
    </header>

    <div class="title">
      <div class="title-main">GARDEN</div>
      <div class="title-sub">Vital Nutrients</div>
    </div>

    <svg class="ingredient-chart" viewBox="-87 -87 174 174" role="img" aria-label="Ingredient share pie chart">
      <path fill="var(--beef)" d="M0 0 L0 84 A84 84 0 0 1 0 -84 Z"/>
      <path fill="var(--chicken)" d="M0 0 L0 -84 A84 84 0 0 1 79.9 -26 Z"/>
      <path fill="var(--rice)" d="M0 0 L79.9 -26 A84 84 0 0 1 68 49.4 Z"/>
      <path fill="var(--veg)" d="M0 0 L68 49.4 A84 84 0 0 1 0 84 Z"/>
      <g stroke="#fff" stroke-width="1.5"><line x1="0" y1="0" x2="0" y2="-84"/><line x1="0" y1="0" x2="79.9" y2="-26"/><line x1="0" y1="0" x2="68" y2="49.4"/><line x1="0" y1="0" x2="0" y2="84"/></g>
      <circle r="84" fill="none" stroke="var(--brand-green)" stroke-width="1.5"/>
      <circle r="3.5" fill="#fff"/>
      <text x="-38" y="1">50%</text>
      <text x="37" y="-39">20%</text>
      <text x="51" y="7">15%</text>
      <text x="30" y="54">15%</text>
    </svg>

    <ul class="ingredient-list">
      <li class="beef">Choice Beef</li>
      <li class="chicken">Pasture-raised Chicken</li>
      <li class="rice">Brown Rice</li>
      <li class="veg">Fresh Vegetables (Car-<br>rots, Kale, Zucchini)</li>
    </ul>

    <ul class="storage">
      <li><svg class="storage-mark" viewBox="0 0 20 20" aria-hidden="true"><path d="M3 10 L8 15 L17 4" fill="none" stroke="var(--green)" stroke-width="3" stroke-linecap="round" stroke-linejoin="round"/></svg>Stores in freezer Up to 6 months</li>
      <li><svg class="storage-mark" viewBox="0 0 20 20" aria-hidden="true"><path d="M3 10 L8 15 L17 4" fill="none" stroke="var(--green)" stroke-width="3" stroke-linecap="round" stroke-linejoin="round"/></svg>Keeps in fridge for 4 days after thawing</li>
    </ul>

    <p class="contact">Questions? E-mail : orders@meadowlanepantry.com</p>

    <p class="website">
      <svg viewBox="0 0 14 14" aria-hidden="true"><g fill="none" stroke="var(--green)" stroke-width="1.2"><circle cx="7" cy="7" r="6"/><ellipse cx="7" cy="7" rx="2.6" ry="6"/><line x1="1" y1="7" x2="13" y2="7"/></g></svg>
      www.pupkitchenmeals.com
    </p>

    <div class="bowl-art" role="img" aria-label="Illustration of a dog food bowl"></div>
    <div class="dog-art" role="img" aria-label="Illustration of a happy yellow puppy wearing a red bandana"></div>
  </main>
</body>
</html>
```